Startup sucht passendes Webdesign
Zielgruppe
Wir produzieren Sand-Steinsedimente zur dekorativen Wand-, Boden- und Fassadengestaltung im Innen- und Außenbereich. Das kann man sich wie eine Tapete vorstellen, halt nur aus Stein. Der Stein ist so dünn, dass das Material bei der Verarbeitung flexibel ist. Nach der Verarbeitung jedoch nicht mehr von einem Steinblock zu unterscheiden.
Die Zielgruppe:
Innenarchitekten, Architekten, Fliesen und Naturstein- Fachmärkte, Entwickler und Planer, Messebauer, Dekorateure, Maler/Tapeten Fachhändler
Da wir in der Gründungsphase sind, gibt es noch keine Onlinepräsenz.
Aufgabenstellung
Die Webseite soll Vertrauen und Exklusivität ausstrahlen. Es geht um das Grundlayout, welches dann später inhouse erweitert werden kann.

```html
<!DOCTYPE html>
<html lang="de">
<head>
<meta charset="utf-8">
<title>Veltrastone</title>
<link href="https://fonts.googleapis.com/css2?family=Arimo:wght@400;700&display=swap" rel="stylesheet">
<style>
:root{
  --navy:#0a4689;
  --blue:#2565a9;
  --steel:#6387aa;
  --stone:#cbcdcb;
  --shadow:#8a8c8e;
  --white:#ffffff;
  --ink:#111111;
}
*{margin:0;padding:0;box-sizing:border-box}
html,body{width:667px;height:1200px;overflow:hidden;background:var(--white)}
body{position:relative;font-family:"Arimo",Arial,sans-serif;color:var(--ink)}
.abs{position:absolute}

.hero{left:0;top:0;width:667px;height:354px;
  background:
    radial-gradient(ellipse 170px 70px at 470px 300px,rgba(236,236,234,.95),rgba(236,236,234,0) 100%),
    radial-gradient(ellipse 120px 50px at 190px 305px,rgba(230,230,228,.9),rgba(230,230,228,0) 100%),
    radial-gradient(ellipse 140px 90px at 600px 270px,rgba(205,205,203,.9),rgba(205,205,203,0) 100%),
    linear-gradient(180deg,rgba(0,0,0,0) 0%,rgba(0,0,0,0) 62%,rgba(40,42,48,.55) 72%,rgba(60,62,66,.35) 100%),
    linear-gradient(90deg,#d9dde0 0%,#b9bfc4 8%,#5b5f66 14%,#8a6c62 20%,#6e6f73 28%,#c2c5c8 42%,#e3e4e5 52%,#514a45 62%,#3e3935 78%,#5c5650 92%,#807a72 100%)}
.topbar{left:0;top:10px;width:667px;height:41px;background:rgba(33,92,158,.88)}
.brand{left:42px;top:10px;width:231px;height:41px;background:rgba(255,255,255,.85);display:flex;align-items:center;gap:8px;padding-left:4px}
.brand-dot{width:36px;height:36px;border-radius:50%;background:var(--navy)}
.brand-name{font-size:21px;color:var(--navy);letter-spacing:1px}
.nav{left:286px;top:22px;display:flex;gap:8px;font-size:13.5px;color:var(--white)}
.search{left:559px;top:22px;width:97px;height:17px;border-radius:4px;background:rgba(120,160,205,.6)}
.search svg{position:absolute;right:6px;top:2px}

.band{left:0;top:354px;width:667px;height:46px;background:var(--navy)}
.stone-area{left:0;top:400px;width:667px;height:428px;background:var(--stone)}
.banner-text{color:var(--white);font-size:23px;letter-spacing:.5px}

.section-title{left:33px;top:443px;font-size:17px;color:var(--navy)}
.section-rule{left:0;top:463px;width:567px;height:4px;background:var(--navy)}
.tile{width:90px;height:88px}
.info{width:26px;height:12px;border-radius:3px;background:var(--navy);color:var(--white);font-size:10px;line-height:12px;text-align:center}

.select{left:501px;top:476px;width:140px;height:172px;background:var(--steel);color:var(--white);padding:5px 5px}
.select-head{font-size:11.5px;border-bottom:1px solid var(--white);width:128px;padding-bottom:1px;margin-bottom:5px}
.select-main{font-size:12.5px;line-height:16px}
.select-sub{font-size:11.5px;line-height:15px;padding-left:19px}

.rule-white{left:100px;top:830px;width:567px;height:5px;background:var(--navy)}
.about-text{left:157px;top:905px;width:428px;font-size:8.3px;line-height:11.3px}
.about-text p+p{margin-top:11px}
.photo{left:0;top:905px;width:146px;height:147px;
  background:
    linear-gradient(180deg,rgba(0,0,0,0) 0%,rgba(0,0,0,0) 78%,#7d7b77 80%,#a09d97 100%),
    linear-gradient(90deg,#b9bdc2 0%,#8b9096 24%,#8a8177 36%,#9a9082 60%,#7f776c 82%,#b7b8b6 92%,#9c9892 100%)}
.grey-rule{left:0;top:1052px;width:570px;height:5px;background:var(--shadow)}

.footer{left:0;top:1057px;width:667px;height:143px;background:var(--navy);color:var(--white)}
.foot-brand{left:46px;top:16px;display:flex;align-items:center;gap:6px}
.foot-dot{width:29px;height:29px;border-radius:50%;background:#c9ccd2}
.foot-name{font-size:17px;color:#c9ccd2;letter-spacing:1px}
.contact{left:46px;top:63px;font-size:8.5px;line-height:11.5px}
.badges{left:47px;top:105px;display:flex;gap:8px}
.badge{width:32px;height:32px;border:2px solid #9aa3ad;border-radius:3px}
.social{left:472px;top:26px;display:flex;gap:14px}
.social span{width:12px;height:12px;border-radius:50%;background:var(--white)}
.find{left:440px;top:50px;width:180px;font-size:8.6px;line-height:11.5px;text-align:right}
</style>
</head>
<body>

<div class="abs hero" role="img" aria-label="Photo of a modern loft living room with stone-clad walls, white sofas and large windows"></div>
<div class="abs topbar"></div>
<div class="abs brand"><span class="brand-dot"></span><span class="brand-name">Veltrastone</span></div>
<nav class="abs nav"><span>Home</span><span>Catalogue</span><span>Designs</span><span>Contact</span><span>About</span></nav>
<div class="abs search"><svg width="13" height="13" viewBox="0 0 13 13"><circle cx="5" cy="5" r="4" fill="none" stroke="#c8d6e6" stroke-width="1.6"/><line x1="8" y1="8" x2="12" y2="12" stroke="#c8d6e6" stroke-width="2"/></svg></div>

<div class="abs band"></div>
<div class="abs stone-area"></div>
<svg class="abs" style="left:336px;top:367px" width="331" height="63" viewBox="0 0 331 63">
  <polygon points="0,7 320,7 272,54 0,54" fill="var(--blue)"/>
  <polygon points="0,54 272,54 268,58 0,58" fill="var(--shadow)"/>
  <polygon points="331,0 331,50 282,50" fill="var(--blue)"/>
  <polygon points="282,50 331,50 331,54 278,54" fill="var(--shadow)"/>
</svg>
<div class="abs banner-text" style="left:354px;top:388px">Sample Text</div>

<div class="abs section-title">Stone Samples</div>
<div class="abs section-rule"></div>

<div class="abs tile" style="left:33px;top:476px;background:linear-gradient(170deg,#968d8a,#857e7c 50%,#8f8785)" role="img" aria-label="Grey stone sample"></div>
<div class="abs tile" style="left:134px;top:476px;background:linear-gradient(135deg,#d5b27c,#c49d66 35%,#dcbb86 60%,#c09a62)" role="img" aria-label="Golden sandstone sample"></div>
<div class="abs tile" style="left:237px;top:476px;background:radial-gradient(circle at 30% 40%,#a39d97,#6f6a66 70%),#7a746e" role="img" aria-label="Rubble stone wall sample"></div>
<div class="abs info" style="left:65px;top:567px">Info</div>
<div class="abs info" style="left:166px;top:567px">Info</div>
<div class="abs info" style="left:270px;top:566px">Info</div>

<div class="abs tile" style="left:33px;top:585px;background:linear-gradient(120deg,#c19a6c,#a98058 40%,#c8a474 70%,#b08a5f)" role="img" aria-label="Banded sandstone tile sample"></div>
<div class="abs tile" style="left:134px;top:585px;background:linear-gradient(160deg,#9a8670,#7f6d5c 50%,#938069)" role="img" aria-label="Weathered brown stone sample"></div>
<div class="abs tile" style="left:237px;top:584px;background:radial-gradient(circle at 60% 50%,#c2beb5,#a7a298 80%)" role="img" aria-label="Light flagstone sample"></div>
<div class="abs info" style="left:65px;top:678px">Info</div>
<div class="abs info" style="left:166px;top:678px">Info</div>
<div class="abs info" style="left:270px;top:678px">Info</div>

<div class="abs tile" style="left:35px;top:697px;background:linear-gradient(180deg,#b98262,#9c6a4f 30%,#c08b6b 55%,#a06e52 80%,#b57e60)" role="img" aria-label="Stacked brick-red stone sample"></div>
<div class="abs tile" style="left:136px;top:697px;background:linear-gradient(180deg,#8a7868,#6c5c4f 35%,#8d7b6a 65%,#6e5e51)" role="img" aria-label="Stacked brown ledgestone sample"></div>
<div class="abs tile" style="left:237px;top:698px;background:radial-gradient(circle at 75% 35%,#b98460 0,#8f8883 45%),#8a847f" role="img" aria-label="Fieldstone wall sample with rust tones"></div>
<div class="abs info" style="left:65px;top:792px">Info</div>
<div class="abs info" style="left:169px;top:792px">Info</div>
<div class="abs info" style="left:270px;top:792px">Info</div>

<div class="abs select">
  <div class="select-head">SELECT</div>
  <div class="select-main">¤Sedimentary</div>
  <div class="select-sub">-Limestone</div>
  <div class="select-sub">-Sandstone</div>
  <div class="select-sub">-Soapstone</div>
  <div class="select-sub">-Fossilstone</div>
  <div class="select-sub">-Travertine</div>
  <div class="select-main">¤Metamorphic</div>
  <div class="select-main">¤Igneous</div>
  <div class="select-main">¤Man Made</div>
</div>

<div class="abs rule-white"></div>
<svg class="abs" style="left:0;top:838px" width="227" height="45" viewBox="0 0 227 45">
  <polygon points="8,6 226,6 226,40 44,40" fill="var(--blue)"/>
  <polygon points="0,2 36,40 0,40" fill="var(--blue)"/>
  <polygon points="0,34 6,40 0,40" fill="var(--white)"/>
  <polygon points="44,40 226,40 226,44 48,44" fill="var(--shadow)"/>
</svg>
<div class="abs banner-text" style="left:114px;top:853px;font-size:17.5px">Sample Text</div>

<div class="abs photo" role="img" aria-label="Photo of a curved house facade clad in grey stone by a lake"></div>
<div class="abs about-text">
  <p>Agreed joy vanity regret met may ladies oppose who. Mile fail as left as hard eyes. Meet made call in mean four year it to. Prospect so branched wondered sensible of up. For gay consisted resolving pronounce sportsman saw discovery not. Northward or household as conveying we earnestly believing. No in up contrasted discretion inhabiting excellence. Entreaties we collecting unpleasant at everything conviction.</p>
  <p>View fine me gone this name an rank. Compact greater and demands mrs the parlors. Park be fine easy am size away. Him and fine bred knew. At of hardly sister favour. As society explain country raising weather of. Sentiments nor everything off out uncommonly partiality bed.</p>
</div>
<div class="abs grey-rule"></div>

<footer class="abs footer">
  <div class="abs foot-brand"><span class="foot-dot"></span><span class="foot-name">Veltrastone</span></div>
  <div class="abs contact">Contact info:<br>t: (+20) 5550 1928<br>e: ouremail@veltrastone.de</div>
  <div class="abs badges"><span class="badge"></span><span class="badge"></span><span class="badge"></span><span class="badge"></span><span class="badge"></span></div>
  <div class="abs social"><span></span><span></span><span></span><span></span><span></span><span></span></div>
  <div class="abs find">Find us online through our net store<br>or other social media</div>
</footer>

</body>
</html>
```